Flyer für Sternenhimmel-Beobachtungen
Zielgruppe
Mit Lumo Vale biete ich geführte Sternenhimmel-Beobachtungen in Hönow (Hoppegarten) an.
Die Teilnehmer erhalten interessante Informationen über den aktuellen Sternenhimmel, astronomische Ereignisse und besondere Himmelsobjekte.
Mit einem großen Teleskop und Ferngläsern beobachten wir Objekte unseres Sonnensystems sowie Sterne, Doppelsterne, Sternhaufen, Nebel und Galaxien.
Je nach Jahreszeit dauern die Touren zwischen 1 und 2 Stunden.
Ausrüstung, Stühle, Decken, Snacks und Tee werden von mir bereitgestellt.
Aufgabenstellung
Gerne maximal 2 Seiten. Mit Informationen auf Vorderseite und Rückseite.

```html
<!DOCTYPE html>
<html lang="de">
<head>
<meta charset="utf-8">
<title>Lumo Vale – Flyer Sternenhimmel-Beobachtungen</title>
<link rel="stylesheet" href="https://fonts.googleapis.com/css2?family=Lato:wght@400;700;900&display=swap">
<style>
  :root {
    --canvas: #dcdcdc;
    --night: #06181a;
    --night-deep: #031011;
    --teal: #2fbfbd;
    --teal-dark: #1c8f8d;
    --white: #ffffff;
    --sky-top: #4a6a72;
    --sky-mid: #7c8f93;
  }
  * { box-sizing: border-box; margin: 0; padding: 0; }
  html, body {
    width: 1200px; height: 1117px; overflow: hidden;
    background: var(--canvas);
    font-family: "Lato", sans-serif;
  }
  .page {
    position: absolute; top: 188px;
    width: 522px; height: 739px;
    overflow: hidden;
    background: var(--night);
    color: var(--white);
  }
  .page--front { left: 63px; }
  .page--back {
    left: 613px;
    background: radial-gradient(ellipse at 70% 30%, #2a2530 0%, #0d1618 45%, var(--night-deep) 100%);
  }

  /* front */
  .hero-photo {
    position: absolute; left: 0; top: 0; width: 522px; height: 340px;
    background: linear-gradient(180deg, var(--sky-top) 0%, var(--sky-mid) 55%, #3b3d3e 78%, var(--night) 100%);
  }
  .brand-mark {
    position: absolute; display: flex; flex-direction: column;
    align-items: center; justify-content: center;
    border-radius: 50%; background: var(--teal); color: var(--night);
    font-weight: 900; text-transform: uppercase;
  }
  .page--front .brand-mark { left: 307px; top: 33px; width: 176px; height: 176px; font-size: 22px; }
  .page--back .brand-mark { left: 381px; top: 23px; width: 120px; height: 120px; font-size: 16px; }

  .headline { position: absolute; left: 0; right: 0; text-align: center; }
  .headline__intro { top: 343px; font-size: 22px; font-weight: 700; }
  .headline__main {
    top: 378px; font-size: 45px; font-weight: 900; line-height: 44px;
    text-transform: uppercase; letter-spacing: -0.5px;
  }
  .headline__main .accent { color: var(--teal); }
  .headline__place { top: 520px; font-size: 22px; font-weight: 700; }
  .lead {
    position: absolute; left: 40px; right: 40px; top: 570px;
    text-align: center; font-size: 16px; line-height: 18px;
  }

  /* footer */
  .footer { position: absolute; left: 0; bottom: 0; width: 522px; height: 80px; }
  .footer svg { position: absolute; left: 0; top: 0; }
  .footer__url {
    position: absolute; left: 0; right: 0; top: 30px; text-align: center;
    font-size: 20px; font-weight: 900; letter-spacing: 4.5px;
  }

  /* back */
  .intro {
    position: absolute; left: 47px; top: 42px; width: 330px;
    font-size: 15.5px; line-height: 17.5px;
  }
  .intro strong { font-weight: 900; }
  .photo-tile {
    position: absolute; left: 53px; width: 186px; height: 143px;
    border: 4px solid var(--teal); border-radius: 12px;
  }
  .photo-tile--nebula { top: 138px; background: linear-gradient(135deg, #3a3f8a, #b35fa8 45%, #e9a86a 70%, #2c3a7c); }
  .photo-tile--moon { top: 293px; background: radial-gradient(circle at 48% 56%, #7d8fc4 0 14%, #1f3a78 15%, #1c336e 100%); }
  .guide-photo {
    position: absolute; left: 250px; top: 107px; width: 272px; height: 344px;
    background: radial-gradient(ellipse at 45% 60%, #1e2325 0%, #121719 55%, rgba(8,20,22,0) 80%);
  }
  .duration-box {
    position: absolute; left: 47px; top: 463px; width: 428px; height: 111px;
    border-radius: 10px;
    background: linear-gradient(180deg, var(--teal) 0%, var(--teal-dark) 100%);
    display: flex; align-items: center; justify-content: center; text-align: center;
    font-size: 27px; line-height: 27px; font-weight: 900; text-transform: uppercase;
  }
  .included {
    position: absolute; left: 30px; right: 30px; top: 603px;
    text-align: center; font-size: 16px; line-height: 21px; font-weight: 700;
    text-transform: uppercase;
  }
</style>
</head>
<body>

<section class="page page--front">
  <div class="hero-photo" role="img" aria-label="Silhouette eines Beobachters mit Teleskop vor Abendhimmel und Baumkronen"></div>
  <div class="brand-mark">Lumo Vale</div>

  <p class="headline headline__intro">MIT LUMO VALE BIETE ICH</p>
  <h1 class="headline headline__main">Geführte<br>Sternenhimmel-<br><span class="accent">Beobachtungen</span></h1>
  <p class="headline headline__place">IN HÖNOW (HOPPEGARTEN) AN.</p>
  <p class="lead">Die Teilnehmer erhalten interessante Informationen über den aktuellen Sternenhimmel, astronomische Ereignisse und besondere Himmelsobjekte.</p>

  <footer class="footer">
    <svg width="522" height="80" viewBox="0 0 522 80">
      <path d="M0 22 Q261 -6 522 22 L522 80 L0 80 Z" fill="var(--night-deep)"/>
      <path d="M0 20 Q261 -8 522 20" fill="none" stroke="var(--teal)" stroke-width="5"/>
    </svg>
    <p class="footer__url">www.lumo-vale.de</p>
  </footer>
</section>

<section class="page page--back">
  <p class="intro">Mit einem großen <strong>Teleskop und Ferngläsern</strong> beobachten wir Objekte unseres Sonnensystems sowie Sterne, Doppelsterne, Sternhaufen, Nebel und Galaxien.</p>
  <div class="brand-mark">Lumo Vale</div>

  <div class="guide-photo" role="img" aria-label="Gastgeber im dunklen Kapuzenpullover mit großem Teleskop"></div>
  <div class="photo-tile photo-tile--nebula" role="img" aria-label="Person vor einer raumfüllenden Projektion eines farbigen Nebels"></div>
  <div class="photo-tile photo-tile--moon" role="img" aria-label="Halbmond am blauen Himmel"></div>

  <p class="duration-box">Je nach Jahreszeit dauern<br>die Touren zwischen<br>1 und 2 Stunden.</p>
  <p class="included">Ausrüstung, Stühle, Decken, Snacks und Tee<br>werden von mir bereitgestellt.</p>

  <footer class="footer">
    <svg width="522" height="80" viewBox="0 0 522 80">
      <path d="M0 22 Q261 -6 522 22 L522 80 L0 80 Z" fill="var(--night-deep)"/>
      <path d="M0 20 Q261 -8 522 20" fill="none" stroke="var(--teal)" stroke-width="5"/>
    </svg>
    <p class="footer__url">www.lumo-vale.de</p>
  </footer>
</section>

</body>
</html>
```